Brightway Haul & Repair Services, are a company that offers a 'one stop shop' pre-move clean up a

I have already selected a logo which I would like on the front of the business cards along with phone numbers, web address and email which are:
0419574302
www.brightwayhaul.com.au
brightwayhaulrepair@mailbox.example

On the back of the card I would like to list some of the types of service we offer (clean - move - repairs/maintenance) which are:
CLEAN - windows, gutters, solar panels, driveways/paths, carpets.
MOVE - Small/medium size house/office moves, large item pick-up & delivery, yard clean-up and removal.
General maintenance and repairs.

I would like the blue logo on a gray background.

Thanks

```html
<!DOCTYPE html>
<html lang="en">
<head>
<meta charset="utf-8">
<title>Brightway Haul &amp; Repair Services – Business Card</title>
<link rel="stylesheet" href="https://fonts.googleapis.com/css2?family=Arimo:wght@400;700&display=swap">
<style>
  :root {
    --page-bg: #e9e7e3;
    --card-grey: #686868;
    --accent-blue: #2e67b8;
    --name-blue: #8dbbe8;
    --text-white: #ffffff;
    --shadow: rgba(0, 0, 0, 0.22);
  }
  * { box-sizing: border-box; margin: 0; padding: 0; }
  html, body {
    width: 1200px;
    height: 900px;
    overflow: hidden;
    background: var(--page-bg);
    font-family: "Arimo", Arial, sans-serif;
  }
  .canvas {
    position: relative;
    width: 1200px;
    height: 900px;
  }
  .card {
    position: absolute;
    left: 290px;
    width: 620px;
    height: 380px;
    background: var(--card-grey);
    color: var(--text-white);
    box-shadow: 0 6px 18px var(--shadow);
    overflow: hidden;
  }
  .card--front { top: 60px; }
  .card--back { top: 470px; }

  .accent-bar {
    position: absolute;
    background: var(--accent-blue);
  }
  .accent-bar--left { left: 26px; width: 34px; bottom: 0; }
  .accent-bar--right { right: 22px; width: 30px; top: 0; }
  .card--front .accent-bar--left { top: 96px; }
  .card--front .accent-bar--right { height: 196px; }
  .card--back .accent-bar--left { top: 118px; }
  .card--back .accent-bar--right { top: 22px; height: 196px; }

  /* Front */
  .contact {
    position: absolute;
    display: flex;
    align-items: center;
    gap: 10px;
    font-weight: 700;
    white-space: nowrap;
  }
  .contact svg { flex: none; }
  .contact--web { left: 118px; top: 96px; font-size: 19px; }
  .contact--phone { left: 400px; top: 214px; font-size: 19px; letter-spacing: 0.5px; }
  .contact--email { left: 86px; top: 318px; font-size: 15px; }

  .brand-name {
    position: absolute;
    left: 118px;
    top: 128px;
    width: 430px;
    color: var(--name-blue);
    font-weight: 700;
    font-size: 40px;
    line-height: 1.02;
    text-transform: uppercase;
    letter-spacing: 0.5px;
  }

  /* Back */
  .services {
    position: absolute;
    left: 80px;
    right: 60px;
    top: 44px;
    text-align: center;
    font-weight: 700;
  }
  .services__watermark {
    position: absolute;
    left: 0;
    right: 0;
    top: 120px;
    text-align: center;
    font-size: 58px;
    font-weight: 700;
    color: var(--name-blue);
    opacity: 0.35;
    text-transform: uppercase;
    letter-spacing: 1px;
  }
  .services__content { position: relative; }
  .services__heading {
    font-size: 26px;
    line-height: 1.1;
    text-transform: uppercase;
  }
  .services__list {
    list-style: none;
    font-size: 17px;
    line-height: 1.35;
    margin-bottom: 6px;
  }
  .services__list li { white-space: pre; }
  .services__closing {
    margin-top: 34px;
    font-size: 26px;
  }
</style>
</head>
<body>
<main class="canvas">

  <section class="card card--front" aria-label="Business card front">
    <div class="accent-bar accent-bar--left"></div>
    <div class="accent-bar accent-bar--right"></div>

    <p class="contact contact--web">
      <svg width="16" height="16" viewBox="0 0 16 16" aria-hidden="true">
        <circle cx="8" cy="8" r="7" fill="none" stroke="#fff" stroke-width="1.6"/>
        <ellipse cx="8" cy="8" rx="3" ry="7" fill="none" stroke="#fff" stroke-width="1.2"/>
        <line x1="1" y1="8" x2="15" y2="8" stroke="#fff" stroke-width="1.2"/>
      </svg>
      www.brightwayhaul.com.au
    </p>

    <h1 class="brand-name">Brightway Haul &amp; Repair Services</h1>

    <p class="contact contact--phone">
      <svg width="30" height="22" viewBox="0 0 30 22" aria-hidden="true">
        <path d="M3 7c0-3 5-5 12-5s12 2 12 5v2h-6V7H9v2H3z" fill="none" stroke="#fff" stroke-width="1.8" stroke-linejoin="round"/>
        <rect x="7" y="10" width="16" height="10" rx="2" fill="none" stroke="#fff" stroke-width="1.8"/>
        <circle cx="15" cy="15" r="2.6" fill="none" stroke="#fff" stroke-width="1.6"/>
      </svg>
      0419574302
    </p>

    <p class="contact contact--email">
      <svg width="40" height="26" viewBox="0 0 40 26" aria-hidden="true">
        <rect x="1.5" y="1.5" width="37" height="23" fill="none" stroke="#fff" stroke-width="2"/>
        <path d="M1.5 1.5 20 15 38.5 1.5M1.5 24.5 15 11M38.5 24.5 25 11" fill="none" stroke="#fff" stroke-width="2"/>
      </svg>
      brightwayhaulrepair@mailbox.example
    </p>
  </section>

  <section class="card card--back" aria-label="Business card back">
    <div class="accent-bar accent-bar--left"></div>
    <div class="accent-bar accent-bar--right"></div>

    <div class="services">
      <div class="services__watermark" aria-hidden="true">Brightway Haul</div>
      <div class="services__content">
        <h2 class="services__heading">Move</h2>
        <ul class="services__list">
          <li>-Small/medium size house    -office moves</li>
          <li>-large item  -pick-up &amp; delivery</li>
          <li>-yard clean-up and removal</li>
        </ul>
        <h2 class="services__heading">Clean</h2>
        <ul class="services__list">
          <li>-driveways/paths   -solar panels   -windows</li>
          <li>-carpets    -gutters</li>
        </ul>
        <h2 class="services__heading services__closing">General Maintenance and Repairs</h2>
      </div>
    </div>
  </section>

</main>
</body>
</html>
```